Quiet Harbor Roasters - Full Brand Packaging Suite (Pods, Boxes, Bags)

Quiet Harbor Roasters is commissioning a complete packaging system for our 12‑roast specialty coffee collection. Each roast is inspired by a Christian ministry, and every package must follow a consistent storytelling structure across all formats: single‑serve pod lids, 12‑count and 24‑count pod boxes, 12 oz bags, and 2 lb bags.Packaging Formats Needed:• Single‑Serve Pod Lids: Circular design featuring roast name, roast type, ministry inspiration, and color theme.
• 12‑Count & 24‑Count Pod Boxes: Full panel design (front, back, sides, top) matching the roast’s identity and ministry story.
• 12 oz Bag: Vertical layout with strong shelf presence, roast color theme, ministry spotlight, and brand story.
• 2 lb Bag: Same design language as the 12 oz bag, scaled appropriately.
Required Panel Structure (applies to every roast):• Front Panel:• Roast Name
• Roast Type
• “Inspired By: [Ministry Name]”
• “Mission Driven | Fueling Global Impact”
• “Brew it. Share it. Fuel the Mission.”

• Side A — Roast Story:
A short, emotionally resonant description connecting the roast’s flavor profile or theme to the ministry’s impact.
• Side B — Ministry Spotlight:
Ministry name, mission summary, and a “Scan to Give” callout with website link.
• Back Panel:• Flavor Notes
• Origin
• Quiet Harbor Roasters Story (provided text stays consistent across all roasts)
• Statement of giving: “50% of net proceeds support our ministry partners + 10% of gross sales from each roast go directly to the ministry it represents.”

Brand Identity:
Quiet Harbor Roasters blends premium specialty coffee with faith‑driven purpose. Designs should feel clean, premium, unified, and visually distinct per roast through color, tone, and ministry theme.Deliverables:• Print‑ready files for all packaging formats
• Editable source files
• Cohesive color system across all 12 roasts
• Consistent layout structure across lids, boxes, and bags
Goal:
Create a unified, premium packaging system that elevates each roast’s identity, communicates its ministry partnership, and strengthens the mission‑driven heart of Quiet Harbor Roasters.

Target Market(s)

Churches

Industry/Entity Type

Churches, ministries, Christian’s

Requirements
Must have
• I’d like the design to look like the AI GENERATED image I had made of the packaging. It looks classy and clean.
Should not have
• Colorful palette, silly pictures, cartons, mascots

```html
<!DOCTYPE html>
<html lang="en">
<head>
<meta charset="utf-8">
<title>Quiet Harbor Roasters – Pod Lid Concept</title>
<link href="https://fonts.googleapis.com/css2?family=Montserrat:wght@500;600;700&family=Playfair+Display:wght@900&family=Poppins:wght@300&display=swap" rel="stylesheet">
<style>
  :root {
    --amber: #FBA800;
    --espresso: #2C1F1A;
    --cream: #F6F2EA;
    --tan: #A07D4F;
    --ink: #111111;
    --rim: #D9D9D9;
    --stage: #FAFAFA;
    --label-grey: #5E5E5E;
    --white: #FFFFFF;
  }
  html, body {
    margin: 0;
    padding: 0;
    width: 1200px;
    height: 1154px;
    overflow: hidden;
    background: var(--white);
  }
  .sheet { display: block; width: 1200px; height: 1154px; }
  .sheet-label {
    font-family: "Poppins", sans-serif;
    font-weight: 300;
    font-size: 40px;
    letter-spacing: 6px;
    fill: var(--label-grey);
  }
  .brand-name {
    font-family: "Playfair Display", serif;
    font-weight: 900;
    fill: var(--ink);
  }
  .roast-name {
    font-family: "Playfair Display", serif;
    font-weight: 900;
    font-size: 138px;
    fill: var(--ink);
  }
  .blend-name {
    font-family: "Montserrat", sans-serif;
    font-weight: 600;
    font-size: 64px;
    letter-spacing: 5px;
    fill: var(--white);
  }
  .roast-type {
    font-family: "Montserrat", sans-serif;
    font-weight: 600;
    font-size: 50px;
    letter-spacing: 9px;
    fill: var(--tan);
  }
  .inspired-label {
    font-family: "Montserrat", sans-serif;
    font-weight: 700;
    font-size: 24px;
    letter-spacing: 1.5px;
    fill: var(--ink);
  }
  .partner-slot {
    font-family: "Montserrat", sans-serif;
    font-weight: 500;
    font-size: 58px;
    letter-spacing: 7px;
    fill: var(--ink);
  }
  .mission-line {
    font-family: "Montserrat", sans-serif;
    font-weight: 600;
    font-size: 30px;
    letter-spacing: 2px;
    fill: var(--white);
  }
  .tagline-arc {
    font-family: "Montserrat", sans-serif;
    font-weight: 600;
    font-size: 31px;
    letter-spacing: 4px;
    fill: var(--ink);
  }
</style>
</head>
<body>
<svg class="sheet" viewBox="0 0 1950 1875" xmlns="http://www.w3.org/2000/svg">
  <defs>
    <clipPath id="lid-face"><circle cx="972" cy="1050" r="590"/></clipPath>
    <clipPath id="lid-ring"><circle cx="972" cy="1050" r="598"/></clipPath>
    <path id="tagline-path" d="M 382 1050 A 588 588 0 0 0 1562 1050"/>
  </defs>

  <!-- Colour variants -->
  <g class="swatches">
    <rect x="99" y="60" width="69" height="68" fill="#FBA800"/>
    <rect x="183" y="60" width="69" height="68" fill="#8A9A44"/>
    <rect x="266" y="60" width="69" height="68" fill="#2F7A78"/>
    <rect x="350" y="60" width="69" height="68" fill="#7F1512"/>
    <rect x="433" y="60" width="69" height="68" fill="#3A5E7C"/>
    <rect x="517" y="60" width="69" height="68" fill="#B07A3E"/>
    <rect x="600" y="60" width="69" height="68" fill="#7AB7D4"/>
    <rect x="684" y="60" width="69" height="68" fill="#63793A"/>
    <rect x="767" y="60" width="69" height="68" fill="#C06216"/>
    <rect x="851" y="60" width="69" height="68" fill="#5A3920"/>
    <rect x="934" y="60" width="69" height="68" fill="#522B4E"/>
    <rect x="1018" y="60" width="69" height="68" fill="#AE531F"/>
  </g>
  <text class="sheet-label" x="97" y="196">COLOR VARIANTS</text>
  <text class="sheet-label" x="1910" y="100" text-anchor="end">POD DESIGN CONCEPT</text>

  <!-- Stage -->
  <rect x="262" y="345" width="1418" height="1420" fill="var(--stage)"/>

  <!-- Lid -->
  <g class="pod-lid">
    <circle cx="972" cy="1050" r="697" fill="var(--rim)"/>
    <circle cx="972" cy="1050" r="636" fill="var(--espresso)"/>
    <circle cx="972" cy="1050" r="598" fill="var(--amber)"/>
    <circle cx="972" cy="1050" r="590" fill="var(--cream)"/>

    <g clip-path="url(#lid-face)">
      <!-- Brand name -->
      <text class="brand-name" x="972" y="700" font-size="112" text-anchor="middle">Quiet Harbor</text>
      <text class="brand-name" x="972" y="800" font-size="66" letter-spacing="14" text-anchor="middle">ROASTERS</text>

      <!-- Roast name -->
      <text class="roast-name" x="975" y="985" text-anchor="middle" textLength="1040" lengthAdjust="spacingAndGlyphs">MORNING LANTERN</text>

      <!-- Blend band -->
      <rect x="300" y="1022" width="1400" height="90" fill="var(--amber)"/>
      <line x1="458" y1="1067" x2="606" y2="1067" stroke="var(--white)" stroke-width="2"/>
      <line x1="1358" y1="1067" x2="1505" y2="1067" stroke="var(--white)" stroke-width="2"/>
      <text class="blend-name" x="985" y="1090" text-anchor="middle">BREAKFAST BLEND</text>

      <!-- Roast type -->
      <circle cx="626" cy="1162" r="8" fill="var(--tan)"/>
      <text class="roast-type" x="972" y="1177" text-anchor="middle">BREAKFAST ROAST</text>
      <circle cx="1318" cy="1162" r="8" fill="var(--tan)"/>
      <line x1="558" y1="1202" x2="1388" y2="1202" stroke="var(--tan)" stroke-width="2"/>

      <!-- Ministry inspiration -->
      <text class="inspired-label" x="593" y="1288">INSPIRED BY:</text>
      <line x1="828" y1="1237" x2="828" y2="1328" stroke="var(--tan)" stroke-width="2"/>
      <text class="partner-slot" x="908" y="1298">LOGO HERE</text>

      <!-- Mission band -->
      <rect x="300" y="1363" width="1400" height="400" fill="var(--espresso)"/>
      <text class="mission-line" x="950" y="1422" text-anchor="middle">MISSION DRIVEN</text>
      <text class="mission-line" x="950" y="1458" text-anchor="middle">FUELING GLOBAL IMPACT</text>
    </g>

    <!-- Tagline cap -->
    <g clip-path="url(#lid-ring)">
      <path d="M 555 1700 L 555 1530 Q 555 1490 605 1490 L 1355 1490 Q 1405 1490 1405 1530 L 1405 1700 Z" fill="var(--amber)"/>
    </g>

    <!-- Coffee bean icon -->
    <g class="bean-icon" transform="rotate(35 987 1560)">
      <ellipse cx="987" cy="1560" rx="29" ry="42" fill="var(--espresso)"/>
      <path d="M 987 1520 C 970 1545, 1004 1575, 987 1600" fill="none" stroke="var(--amber)" stroke-width="7" stroke-linecap="round"/>
    </g>

    <text class="tagline-arc"><textPath href="#tagline-path" startOffset="50%" text-anchor="middle">BREW IT. SHARE IT. FUEL THE MISSION.</textPath></text>
  </g>
</svg>
</body>
</html>
```